BrivoMatex. Lantern for the Steady Growth. Business card

Professional business card for BrivoMatex (Lantern for the Steady Growth)
My rationale: Strategy-> Execution-> Results-> Value that lead to the BrivoMatex name: We put the Lantern for the Steady Growth.
We deliver value to our customers helping them at defining a good strategy (cyan arrow). 90% of well formulated strategies fail due to poor execution so we also consider strategical execution very important (green arrow). Due to the execution we obtain the results (blue arrow). Finally, the results provide feedback to redefine strategy, and the new strategy has to be executed and new results obtained providing new feedback and on and on. It's like a wheel that finally, must create corporate value: value for shareholders, staholders, employees, providers...-

Target Market(s)

CEOs and steering comitees , invewrnent funds

Industry/Entity Type

Business Consultant

Contact Information for Business Card

Tommaso Ferlini
CEO & Founder
tommaso.ferlini@brivomatex.example
Mobile: +34 611.205.938
www.brivomatex.example

Colors

Designer to choose colors to be used in the design.

Requirements
Nice to have
• Nice to hace the words: Strategy, execution, results
• Nice to vave the claim: Lantern for the Steady Growth
• The three colors should be shown:
• cyan for STRATEGY
• green for EXECUTION
• blue for RESULTS
Should not have
• Complete black background

```html
<!DOCTYPE html>
<html lang="en">
<head>
<meta charset="utf-8">
<title>BrivoMatex — Business Card</title>
<link rel="stylesheet" href="https://fonts.googleapis.com/css2?family=Roboto:ital,wght@0,400;0,500;0,700;1,400&display=swap">
<style>
  :root {
    --backdrop: #e9e6e1;
    --brand-blue: #2a4a9e;
    --brand-navy: #24408f;
    --brand-green: #8dc63f;
    --brand-cyan: #29abe2;
    --card-white: #fbfbfb;
    --ink: #2b2b2b;
    --muted: #3c3c3c;
  }
  * { margin: 0; padding: 0; box-sizing: border-box; }
  html, body {
    width: 1200px;
    height: 900px;
    overflow: hidden;
    background: var(--backdrop);
    font-family: "Roboto", Arial, sans-serif;
  }
  .stage {
    position: relative;
    width: 1200px;
    height: 900px;
  }
  .card {
    position: absolute;
    width: 630px;
    height: 360px;
    border-radius: 4px;
    box-shadow: 0 10px 28px rgba(0, 0, 0, 0.18);
  }

  /* Front: brand side */
  .card-front {
    left: 320px;
    top: 70px;
    background: var(--brand-blue);
    display: flex;
    flex-direction: column;
    align-items: center;
    justify-content: center;
    text-align: center;
  }
  .front-name {
    color: #ffffff;
    font-weight: 700;
    font-size: 66px;
    letter-spacing: -1px;
    line-height: 1;
  }
  .front-claim {
    margin-top: 12px;
    color: var(--brand-green);
    font-weight: 500;
    font-size: 19px;
    letter-spacing: 0.6px;
    text-transform: uppercase;
  }
  .front-pillars {
    margin-top: 6px;
    color: var(--brand-cyan);
    font-weight: 500;
    font-size: 19px;
    letter-spacing: 0.8px;
    text-transform: uppercase;
  }
  .front-pillars .divider { padding: 0 8px; }

  /* Back: contact side */
  .card-back {
    left: 250px;
    top: 470px;
    background: var(--card-white);
    padding: 46px 56px;
  }
  .back-brand {
    display: flex;
    align-items: center;
    gap: 14px;
  }
  .back-brand .dot {
    width: 18px;
    height: 18px;
    border-radius: 50%;
    background: var(--brand-navy);
  }
  .back-name {
    color: var(--brand-navy);
    font-weight: 700;
    font-size: 40px;
    letter-spacing: -0.5px;
  }
  .person {
    margin-top: 44px;
  }
  .person-name {
    color: var(--brand-cyan);
    font-weight: 700;
    font-size: 19px;
    letter-spacing: 0.8px;
    text-transform: uppercase;
  }
  .person-role {
    margin-top: 3px;
    color: var(--muted);
    font-size: 12.5px;
    text-transform: uppercase;
  }
  .contact-list {
    list-style: none;
    margin-top: 28px;
  }
  .contact-list li {
    display: flex;
    align-items: center;
    gap: 12px;
    color: var(--ink);
    font-size: 17px;
    margin-bottom: 7px;
  }
  .contact-list .email { font-style: italic; }
  .contact-list svg {
    width: 18px;
    height: 18px;
    flex: none;
  }
</style>
</head>
<body>
<main class="stage">

  <section class="card card-front" aria-label="Business card front">
    <div class="front-name">BrivoMatex</div>
    <div class="front-claim">Lantern for the Steady Growth</div>
    <div class="front-pillars">Strategy<span class="divider">|</span>Execution<span class="divider">|</span>Results</div>
  </section>

  <section class="card card-back" aria-label="Business card back">
    <div class="back-brand">
      <span class="dot"></span>
      <span class="back-name">BrivoMatex</span>
    </div>

    <div class="person">
      <div class="person-name">Tommaso Ferlini</div>
      <div class="person-role">CEO &amp; Founder</div>
    </div>

    <ul class="contact-list">
      <li>
        <svg viewBox="0 0 18 18" aria-hidden="true">
          <rect x="5" y="1.5" width="8" height="15" rx="1.5" fill="none" stroke="var(--brand-cyan)" stroke-width="1.6"/>
          <circle cx="9" cy="13.8" r="0.9" fill="var(--brand-cyan)"/>
        </svg>
        <span>+34 611 205 938</span>
      </li>
      <li>
        <svg viewBox="0 0 18 18" aria-hidden="true">
          <rect x="1.5" y="4" width="15" height="10" rx="1" fill="var(--brand-cyan)"/>
          <path d="M1.8 4.5 L9 10 L16.2 4.5" fill="none" stroke="#ffffff" stroke-width="1.3"/>
        </svg>
        <span class="email">tommaso.ferlini@brivomatex.example</span>
      </li>
      <li>
        <svg viewBox="0 0 18 18" aria-hidden="true">
          <circle cx="9" cy="9" r="7.5" fill="var(--brand-cyan)"/>
          <path d="M9 1.5 C5.5 5 5.5 13 9 16.5 M9 1.5 C12.5 5 12.5 13 9 16.5 M1.5 9 H16.5" fill="none" stroke="#ffffff" stroke-width="1.1"/>
        </svg>
        <span>www.brivomatex.example</span>
      </li>
    </ul>
  </section>

</main>
</body>
</html>
```